Design of an attractive membership brochure/membership card for an Electrical Business

Hi, we are an electrical business based in Sydney, Australia.

Our design's aim is to attract and target new customers into using our business as a repeat for anything electrical in their home. We would be handing this out to them after a job is completed and they're happy with the service.
We're thinking of a brochure, possibly additional membership cards with personalized number ID's for each client.

Open to ideas, but some of the things we want to include on our brochure are perks of why the client should sign up with us as a lifetime client
- Discounted emergency call out fees outside of normal hours
- Lifetime membership price, one time payment
- Exclusive 10% member discount on all future jobs
- Priority on any during business hour jobs or emergencies

If any other questions please don't hesitate to reach out.
We've attached our logo for reference for the mock designs.
Our website
https://brightwirehaus.com.au/

```html
<!DOCTYPE html>
<html lang="en">
<head>
<meta charset="utf-8">
<title>Brightwire Haus – Membership Brochure</title>
<link href="https://fonts.googleapis.com/css2?family=Montserrat:wght@400;500;600;700;800;900&display=swap" rel="stylesheet">
<style>
  :root{
    --red:#e1262b;
    --red-deep:#b8161b;
    --ink:#161616;
    --charcoal:#242424;
    --paper:#ffffff;
    --mist:#ececec;
    --stage:#a9a9a9;
    --muted:#444444;
  }
  *{box-sizing:border-box;margin:0;padding:0}
  html,body{width:803px;height:1200px;overflow:hidden}
  body{background:var(--stage);font-family:'Montserrat',sans-serif;position:relative}
  .spread{position:absolute;left:20px;width:763px;height:540px;background:var(--paper);overflow:hidden;box-shadow:0 4px 14px rgba(0,0,0,.25)}
  .spread--outside{top:20px}
  .spread--inside{top:620px}
  .spread svg.art{position:absolute;inset:0;width:763px;height:540px}
  .txt{position:absolute;white-space:nowrap}

  /* wordmark stand-in */
  .wordmark{position:absolute;display:flex;align-items:center;gap:8px;font-weight:800;color:var(--red);letter-spacing:.5px;text-transform:uppercase}
  .wordmark__square{background:var(--red);display:block}
  .wordmark--front{left:470px;top:48px;font-size:27px}
  .wordmark--front .wordmark__square{width:22px;height:22px}
  .wordmark--back{left:92px;top:470px;font-size:20px}
  .wordmark--back .wordmark__square{width:16px;height:16px}

  /* contact panel */
  .contact-title{left:142px;top:226px;font-size:20px;font-weight:800;color:var(--paper)}
  .contact-title__rule{position:absolute;left:73px;top:240px;width:60px;height:2px;background:var(--paper)}
  .contact-name{top:255px;font-size:10px;color:var(--paper);font-weight:500}
  .contact-line{left:73px;font-size:12px;font-weight:700;color:var(--paper);display:flex;align-items:center;gap:9px}
  .contact-line svg{width:12px;height:12px;flex:none}
  .contact-phones{top:267px}
  .contact-web{top:291px}
  .contact-mail{top:315px}
  .contact-abn{top:339px}
  .contact-licence{top:362px;line-height:15px;align-items:flex-start}

  /* front cover */
  .headline{left:420px;top:400px;color:var(--paper);font-weight:900;line-height:36px;font-size:33px}
  .headline__accent{color:var(--red);font-size:40px}
  .cover-url{left:465px;width:298px;top:505px;text-align:center;font-size:13px;font-weight:700;color:var(--paper)}

  /* about */
  .section-title{font-size:20px;font-weight:900;color:var(--paper)}
  .about-title{left:44px;top:28px}
  .about-title__rule{position:absolute;left:44px;top:55px;width:240px;height:1.5px;background:rgba(255,255,255,.8)}
  .about-copy{position:absolute;left:44px;top:68px;width:318px;font-size:7.1px;line-height:9.1px;font-weight:600;color:var(--paper)}
  .about-copy p+p{margin-top:9px}

  /* perks */
  .perks-title{left:44px;top:362px;font-size:14px;font-weight:800;color:var(--paper);line-height:18px}
  .perks-title__rule{position:absolute;left:44px;top:405px;width:292px;height:1.5px;background:var(--mist)}
  .perks{position:absolute;left:44px;top:424px;list-style:none}
  .perks li{display:flex;align-items:center;gap:9px;font-size:9.2px;font-weight:500;color:var(--paper);height:23.5px}
  .perks li::before{content:"";width:5px;height:5px;border-top:1.8px solid var(--red);border-right:1.8px solid var(--red);transform:rotate(45deg)}

  /* services */
  .services-title{left:415px;top:28px;font-size:20px;font-weight:900;color:var(--ink)}
  .services-title span{color:var(--red)}
  .services-sub{left:415px;top:54px;font-size:10.5px;font-weight:500;color:var(--muted)}
  .services-rule{position:absolute;left:415px;top:80px;width:260px;height:1.5px;background:var(--red)}
  .service{position:absolute;font-size:10.5px;line-height:12px;font-weight:500;color:var(--ink);transform:translateY(-50%)}
</style>
</head>
<body>

<!-- ============ OUTSIDE SPREAD: back panel + front cover ============ -->
<section class="spread spread--outside">
  <svg class="art" viewBox="0 0 763 540" aria-hidden="false">
    <defs>
      <linearGradient id="gHall" x1="0" y1="0" x2="1" y2="1">
        <stop offset="0" stop-color="#d8dce1"/><stop offset=".45" stop-color="#2a2f35"/><stop offset="1" stop-color="#9aa1a8"/>
      </linearGradient>
      <linearGradient id="gBath" x1="0" y1="0" x2="0" y2="1">
        <stop offset="0" stop-color="#f3f1ec"/><stop offset=".6" stop-color="#ddd3c3"/><stop offset="1" stop-color="#a88a62"/>
      </linearGradient>
      <linearGradient id="gLiving" x1="0" y1="0" x2="0" y2="1">
        <stop offset="0" stop-color="#ece8e3"/><stop offset=".5" stop-color="#c9b59c"/><stop offset="1" stop-color="#8a6246"/>
      </linearGradient>
      <linearGradient id="gBlack" x1="0" y1="0" x2="1" y2="1">
        <stop offset="0" stop-color="#2a2a2a"/><stop offset="1" stop-color="#0f0f0f"/>
      </linearGradient>
    </defs>

    <!-- back panel photos -->
    <g role="img" aria-label="Photo of a modern hallway with a crystal chandelier">
      <polygon points="0,0 186,0 186,200 0,230" fill="url(#gHall)"/>
    </g>
    <g role="img" aria-label="Photo of a bright bathroom with a window and timber vanity">
      <polygon points="189,0 381,0 381,150 189,200" fill="url(#gBath)"/>
    </g>
    <!-- back panel bands -->
    <polygon points="0,205 381,145 381,168 0,225" fill="var(--paper)"/>
    <polygon points="0,225 381,168 381,393 0,437" fill="var(--red)"/>
    <polygon points="0,437 381,393 381,404 0,450" fill="#dcdcdc"/>

    <!-- front cover -->
    <polygon points="381,168 763,108 763,118 381,176" fill="#cfcfcf"/>
    <g role="img" aria-label="Photo of a warmly lit living room with downlights and a sofa">
      <polygon points="381,176 763,118 763,326 381,352" fill="url(#gLiving)"/>
    </g>
    <polygon points="381,352 763,326 763,540 381,540" fill="url(#gBlack)"/>
    <polygon points="560,342 763,322 763,334 590,350" fill="#7a7a7a"/>
    <polygon points="478,497 763,490 763,540 465,540" fill="var(--red)"/>

    <!-- corner bracket -->
    <path d="M713 14 H745 V62" fill="none" stroke="var(--ink)" stroke-width="3"/>
    <path d="M745 66 V78" stroke="var(--red)" stroke-width="3"/>
  </svg>

  <!-- back panel: contact -->
  <span class="contact-title__rule"></span>
  <div class="txt contact-title">GET IN CONTACT</div>
  <div class="txt contact-name" style="left:73px">Marcus Lee</div>
  <div class="txt contact-name" style="left:202px">Owen Park</div>
  <div class="txt contact-line contact-phones">
    <svg viewBox="0 0 12 12"><circle cx="6" cy="6" r="6" fill="#fff"/><path d="M4 3.2l1 1.6-.6.7c.4.8 1 1.4 1.8 1.8l.7-.6 1.6 1-.5 1.1C5.6 8.6 3.4 6.4 3 4.1z" fill="var(--red)"/></svg>
    0400 555 120 &nbsp;|&nbsp;
    <svg viewBox="0 0 12 12"><circle cx="6" cy="6" r="6" fill="#fff"/><path d="M4 3.2l1 1.6-.6.7c.4.8 1 1.4 1.8 1.8l.7-.6 1.6 1-.5 1.1C5.6 8.6 3.4 6.4 3 4.1z" fill="var(--red)"/></svg>
    0400 555 134
  </div>
  <div class="txt contact-line contact-web">
    <svg viewBox="0 0 12 12"><circle cx="6" cy="6" r="6" fill="#fff"/><circle cx="6" cy="6" r="3.2" fill="none" stroke="var(--red)" stroke-width="1"/><path d="M2.8 6h6.4M6 2.8v6.4" stroke="var(--red)" stroke-width=".8"/></svg>
    www.brightwirehaus.com.au
  </div>
  <div class="txt contact-line contact-mail">
    <svg viewBox="0 0 12 12"><circle cx="6" cy="6" r="6" fill="#fff"/><rect x="3" y="4" width="6" height="4.2" fill="none" stroke="var(--red)" stroke-width="1"/><path d="M3 4l3 2.3L9 4" fill="none" stroke="var(--red)" stroke-width="1"/></svg>
    services@brightwirehaus.com.au
  </div>
  <div class="txt contact-line contact-abn">
    <svg viewBox="0 0 12 12"><path d="M3.5 2l4 4-4 4" fill="none" stroke="#fff" stroke-width="2"/></svg>
    ABN - 12 345 678 901
  </div>
  <div class="txt contact-line contact-licence">
    <svg viewBox="0 0 12 12"><path d="M7.5 0L2 7h3.5L4 12l6-7.5H6.5z" fill="#fff"/></svg>
    <span>Electrical Contractor Licence<br>No.281734E</span>
  </div>

  <div class="wordmark wordmark--back"><span class="wordmark__square"></span>Brightwire Haus</div>

  <!-- front cover -->
  <div class="wordmark wordmark--front"><span class="wordmark__square"></span>Brightwire Haus</div>
  <div class="txt headline"><span class="headline__accent">24/7</span> SYDNEY<br>ELECTRICIANS</div>
  <div class="txt cover-url">www.brightwirehaus.com.au</div>
</section>

<!-- ============ INSIDE SPREAD: about + services ============ -->
<section class="spread spread--inside">
  <svg class="art" viewBox="0 0 763 540">
    <defs>
      <linearGradient id="gRoom" x1="0" y1="0" x2="1" y2="1">
        <stop offset="0" stop-color="#e9ecef"/><stop offset="1" stop-color="#7d8792"/>
      </linearGradient>
      <linearGradient id="gKitchenWhite" x1="0" y1="0" x2="0" y2="1">
        <stop offset="0" stop-color="#f4f3f0"/><stop offset="1" stop-color="#8b7560"/>
      </linearGradient>
      <linearGradient id="gKitchenBlue" x1="0" y1="0" x2="1" y2="1">
        <stop offset="0" stop-color="#3d4f63"/><stop offset="1" stop-color="#1d2630"/>
      </linearGradient>
      <linearGradient id="gSink" x1="0" y1="0" x2="1" y2="0">
        <stop offset="0" stop-color="#c99a5e"/><stop offset=".5" stop-color="#5b4534"/><stop offset="1" stop-color="#2b241f"/>
      </linearGradient>
      <linearGradient id="gDark" x1="0" y1="0" x2="0" y2="1">
        <stop offset="0" stop-color="#2b2b2b"/><stop offset="1" stop-color="#121212"/>
      </linearGradient>
    </defs>

    <polygon points="0,0 381,0 381,180 0,214" fill="var(--red)"/>
    <g role="img" aria-label="Photo of a living room with a grey sofa">
      <polygon points="0,222 115,211 115,331 0,345" fill="url(#gRoom)"/>
    </g>
    <g role="img" aria-label="Photo of a white kitchen with pendant lights and bar stools">
      <polygon points="118,211 233,200 233,317 118,331" fill="url(#gKitchenWhite)"/>
    </g>
    <g role="img" aria-label="Photo of a blue kitchen with a round dining table">
      <polygon points="236,200 381,186 381,300 236,317" fill="url(#gKitchenBlue)"/>
    </g>
    <polygon points="0,350 381,306 381,540 0,540" fill="url(#gDark)"/>

    <g role="img" aria-label="Photo of a kitchen bench with fresh produce and a black sink">
      <polygon points="381,450 763,405 763,540 381,540" fill="url(#gSink)"/>
    </g>

    <path d="M715 14 H749 V62" fill="none" stroke="var(--ink)" stroke-width="3"/>
    <path d="M749 66 V78" stroke="var(--red)" stroke-width="3"/>

    <!-- service icons -->
    <g id="icons" fill="none" stroke="#fff" stroke-width="1.4" stroke-linecap="round" stroke-linejoin="round">
      <g transform="translate(437 126)"><circle r="19" fill="var(--red)" stroke="none"/><circle r="16.5" fill="#fff" stroke="none"/><circle r="15" fill="var(--ink)" stroke="none"/>
        <circle cy="-1" r="4.5"/><path d="M-2 4v3h4v-3"/></g>
      <g transform="translate(437 177)"><circle r="19" fill="var(--red)" stroke="none"/><circle r="16.5" fill="#fff" stroke="none"/><circle r="15" fill="var(--ink)" stroke="none"/>
        <rect x="-6" y="-6" width="12" height="12" rx="2"/><path d="M-2 -2v2M2 -2v2M0 3v.5"/></g>
      <g transform="translate(437 230)"><circle r="19" fill="var(--red)" stroke="none"/><circle r="16.5" fill="#fff" stroke="none"/><circle r="15" fill="var(--ink)" stroke="none"/>
        <path d="M1.5 -7l-5 7.5h4l-1.5 6.5 5.5-8h-4z" fill="#fff" stroke="none"/></g>
      <g transform="translate(437 284)"><circle r="19" fill="var(--red)" stroke="none"/><circle r="16.5" fill="#fff" stroke="none"/><circle r="15" fill="var(--ink)" stroke="none"/>
        <circle r="7"/><path d="M0 -4v4l3 2"/></g>
      <g transform="translate(437 337)"><circle r="19" fill="var(--red)" stroke="none"/><circle r="16.5" fill="#fff" stroke="none"/><circle r="15" fill="var(--ink)" stroke="none"/>
        <rect x="-7" y="-6" width="14" height="12" rx="1"/><path d="M-4 -2h8M-4 1h8M-4 4h5"/></g>
      <g transform="translate(437 390)"><circle r="19" fill="var(--red)" stroke="none"/><circle r="16.5" fill="#fff" stroke="none"/><circle r="15" fill="var(--ink)" stroke="none"/>
        <path d="M-7 0l7-6 7 6M-5 -1.5v7.5h10v-7.5M-1.5 6v-4h3v4"/></g>

      <g transform="translate(601 126)"><circle r="19" fill="var(--red)" stroke="none"/><circle r="16.5" fill="#fff" stroke="none"/><circle r="15" fill="var(--ink)" stroke="none"/>
        <rect x="-7" y="-5" width="14" height="10" rx="1"/><path d="M-4 -1.5h2M1 -1.5h3M-4 1.5h8"/></g>
      <g transform="translate(601 177)"><circle r="19" fill="var(--red)" stroke="none"/><circle r="16.5" fill="#fff" stroke="none"/><circle r="15" fill="var(--ink)" stroke="none"/>
        <path d="M0 -8v16M-6 -5h12M-4 -2h8M-4 8h8"/></g>
      <g transform="translate(601 230)"><circle r="19" fill="var(--red)" stroke="none"/><circle r="16.5" fill="#fff" stroke="none"/><circle r="15" fill="var(--ink)" stroke="none"/>
        <path d="M-7 3v-3l2-4h10l2 4v3z"/><circle cx="-4" cy="4" r="1.3"/><circle cx="4" cy="4" r="1.3"/></g>
      <g transform="translate(601 284)"><circle r="19" fill="var(--red)" stroke="none"/><circle r="16.5" fill="#fff" stroke="none"/><circle r="15" fill="var(--ink)" stroke="none"/>
        <path d="M-7 -5h14l-2 3h-10z"/><path d="M-3 1q1.5 1.5 0 3M0 1q1.5 1.5 0 3M3 1q1.5 1.5 0 3"/></g>
      <g transform="translate(601 337)"><circle r="19" fill="var(--red)" stroke="none"/><circle r="16.5" fill="#fff" stroke="none"/><circle r="15" fill="var(--ink)" stroke="none"/>
        <circle r="1.8"/><path d="M0 -2q-1 -6 4 -6M2 1q6 -1 6 4M-2 1q-5 4 -6 0"/></g>
    </g>
  </svg>

  <!-- about -->
  <div class="txt section-title about-title">ABOUT US</div>
  <span class="about-title__rule"></span>
  <div class="about-copy">
    <p>Brightwire Haus is a Sydney-based electrical business specialising in electrical maintenance work for residential, commercial, strata and real estate clients. It began with two mates with a strong desire to change the image of tradies and provide exceptional service. As a team of electricians based in the Inner West of Sydney, we understand the need of everyday people struggling to find good, reliable and trustworthy electricians.</p>
    <p>At Brightwire Haus, we have high expectations of ourselves and strive to improve every day. We're always available around the clock to provide professional advice or give a helping hand when in need.</p>
  </div>

  <!-- perks -->
  <div class="txt perks-title">Why the client should sign up with us<br>as a lifetime client</div>
  <span class="perks-title__rule"></span>
  <ul class="perks">
    <li>Discounted emergency call out fees outside of normal hours</li>
    <li>Lifetime membership price, one time payment</li>
    <li>Exclusive 10% member discount on all future jobs</li>
    <li>Priority on any during business hour jobs or emergencies</li>
  </ul>

  <!-- services -->
  <div class="txt services-title">OUR <span>SERVICES</span></div>
  <div class="txt services-sub">Customer Satisfaction Is Our Highest Priority</div>
  <span class="services-rule"></span>

  <div class="service" style="left:467px;top:126px">Light<br>Installation</div>
  <div class="service" style="left:467px;top:177px">Power Outlets</div>
  <div class="service" style="left:467px;top:230px">Surge<br>Protection</div>
  <div class="service" style="left:467px;top:284px">24/7<br>Emergency<br>Services</div>
  <div class="service" style="left:467px;top:337px">Electric Hot<br>Water Repairs</div>
  <div class="service" style="left:467px;top:390px;white-space:nowrap">Real estate, Strata and Commercial</div>

  <div class="service" style="left:631px;top:126px">Switchboard<br>Install, Upgrade<br>&amp; Repair</div>
  <div class="service" style="left:631px;top:177px">Level 2 ASP</div>
  <div class="service" style="left:631px;top:230px">EV Electric<br>Vehicle Charging<br>Stations</div>
  <div class="service" style="left:631px;top:284px">Smoke Alarms</div>
  <div class="service" style="left:631px;top:337px">Ceiling &amp;<br>Exhaust Fans</div>
</section>

</body>
</html>
```